Emergency Dental Referral Company

I need a brochure to advertise my business to prospective dentists that may want to join or to dentists that may want to use this for their own patients. I also need to advertise this brochure to ER physicians who see many dental emergencies. This brochure is meant to be dual purpose: advertise our company and services to the ER physicians who then hand out the brochures to the dental emergency patients in pain. See our website for further details at www.molarrelieffast.net

I will also be attaching our logo design.

Target Market(s)

Emergency Room physicians and other medical personnel who will distribute these brochures to patients in dental pain and dental emergencies

Industry/Entity Type

Business

Font styles to use
Serif
Sans Serif

Requirements
Must have
• Must be simple! Must have a call to action- inspiration to go to website. Highlight our guarantee that states "If you are not seen by a dentist in 24 hours or less, you will receive your money back. Emphasis on the logo. Must discuss how we find a dentist in your zip code in three easy steps.
• For the color- please make similar to our website of www.molarrelieffast.net
Nice to have
• Would like to state that this service can see patients at any hour of the day.
Should not have
• no contact information besides the URL. www.molarrelieffast.net

```html
<!DOCTYPE html>
<html lang="en">
<head>
<meta charset="utf-8">
<title>Molar Relief Fast – Tri-fold Brochure</title>
<link href="https://fonts.googleapis.com/css2?family=Source+Sans+3:wght@400;600;700;900&display=swap" rel="stylesheet">
<style>
  :root{
    --green:#3cb54a;
    --green-dark:#2e9a3c;
    --blue:#1f6fc0;
    --blue-dark:#175aa0;
    --white:#ffffff;
    --ink:#5a5f66;
    --stage:#e4e5e7;
    --photo-a:#f3ece6;
    --photo-b:#d9c4b2;
  }
  *{box-sizing:border-box;margin:0;padding:0}
  html,body{width:1033px;height:1200px;overflow:hidden}
  body{background:var(--stage);font-family:"Source Sans 3",Arial,sans-serif;position:relative}
  .spread{position:absolute;left:36px;width:960px;height:560px;background:var(--white);box-shadow:0 4px 14px rgba(0,0,0,.18);overflow:hidden}
  .spread--outside{top:24px}
  .spread--inside{top:616px}
  .panel{position:absolute;top:0;width:320px;height:560px}
  .panel--1{left:0}.panel--2{left:320px}.panel--3{left:640px}
  .fold{position:absolute;top:0;width:1px;height:560px;background:rgba(0,0,0,.08)}

  /* outside: steps panel */
  .steps-panel{background:var(--green);color:var(--white)}
  .steps-title__num{position:absolute;left:14px;top:-22px;font-size:180px;font-weight:900;line-height:1}
  .steps-title__lead{position:absolute;left:128px;top:22px;font-size:28px;font-weight:600;letter-spacing:.5px}
  .steps-title__box{position:absolute;left:118px;top:58px;width:184px;padding:6px 10px;background:var(--blue);font-size:40px;font-weight:700;line-height:1;text-align:center}
  .steps-title__box::after{content:"";position:absolute;left:80px;bottom:-14px;border:14px solid transparent;border-bottom:0;border-top-color:var(--blue)}
  .step{position:absolute;left:18px;width:284px;height:48px}
  .step__pill{position:absolute;left:30px;top:4px;right:0;height:40px;background:var(--white);border-radius:20px;display:flex;align-items:center;padding-left:44px}
  .step__icon{width:30px;height:30px;flex:none}
  .step__text{flex:1;text-align:center;color:var(--green-dark);font-size:15px;font-weight:600;line-height:1.1}
  .step__num{position:absolute;left:0;top:0;width:48px;height:48px;border-radius:50%;background:var(--blue);border:3px solid var(--white);color:var(--white);font-size:28px;font-weight:700;display:flex;align-items:center;justify-content:center}
  .guarantee{position:absolute}
  .guarantee--steps{left:100px;top:378px;width:120px;height:112px}
  .guarantee--inside{left:210px;top:10px;width:96px;height:90px}
  .steps-panel__note{position:absolute;left:20px;right:20px;top:498px;text-align:center;font-size:16px;line-height:1.25}

  /* outside: middle + cover */
  .brand{display:flex;align-items:center;gap:8px;color:var(--blue);font-weight:700}
  .brand__dot{border-radius:50%;background:var(--green);flex:none}
  .brand--small{position:absolute;left:22px;top:22px;font-size:22px}
  .brand--small .brand__dot{width:22px;height:22px}
  .photo{position:absolute;background:linear-gradient(160deg,var(--photo-a),var(--photo-b))}
  .photo--family{left:320px;top:96px;width:640px;height:304px}
  .middle-band{position:absolute;left:320px;top:0;width:320px;height:560px}
  .service-badge{position:absolute;left:350px;top:370px;width:64px;height:80px}
  .middle-url{position:absolute;left:320px;width:320px;top:512px;text-align:center;color:var(--white);font-size:17px;font-weight:600}
  .cover-title{position:absolute;left:640px;top:14px;width:320px;text-align:center;line-height:1}
  .cover-title__your{color:var(--blue);font-size:34px;font-weight:700}
  .cover-title__emergency{color:var(--green);font-size:34px;font-weight:700}
  .cover-title__dentist{color:var(--blue);font-size:42px;font-weight:900}
  .cover-logo{position:absolute;left:640px;top:420px;width:320px;display:flex;flex-direction:column;align-items:center}
  .brand--large{font-size:30px}
  .brand--large .brand__dot{width:30px;height:30px}
  .cover-url{margin-top:28px;color:var(--blue);font-size:19px;font-weight:700}

  /* inside */
  .about{background:var(--white);padding:22px 22px 0;text-align:center}
  .about p{font-size:13.5px;line-height:1.22;margin-bottom:9px}
  .about .green{color:var(--green-dark)}
  .about .blue{color:var(--blue)}
  .about .lead{color:var(--blue);font-size:17px;font-weight:700;line-height:1.15}
  .brand--about{position:absolute;left:22px;top:500px;font-size:24px}
  .brand--about .brand__dot{width:24px;height:24px}
  .inside-green{position:absolute;left:320px;top:0;width:640px;height:560px;background:var(--green)}
  .inside-heading{position:absolute;left:340px;width:300px;top:24px;text-align:center;color:var(--white);font-size:20px;line-height:1.15}
  .photo--presenter{left:340px;top:90px;width:130px;height:380px;border-radius:60px 60px 4px 4px}
  .issue{position:absolute;height:70px;width:200px}
  .issue__box{position:absolute;left:26px;top:0;right:0;height:62px;background:var(--white);border-radius:14px;display:flex;align-items:center;padding-left:34px;color:var(--green-dark);font-size:17px;line-height:1.1}
  .issue__num{position:absolute;left:0;top:24px;width:46px;height:46px;border-radius:50%;background:var(--blue);border:3px solid var(--white);color:var(--white);font-size:28px;font-weight:700;display:flex;align-items:center;justify-content:center}
  .issue--1{left:442px;top:102px}.issue--3{left:442px;top:204px}.issue--5{left:442px;top:306px}
  .issue--2{left:700px;top:92px;width:240px}.issue--4{left:700px;top:194px;width:240px}.issue--6{left:700px;top:296px;width:240px}
  .service-band{position:absolute;left:320px;top:470px;width:640px;height:48px;background:var(--blue);color:var(--white);display:flex;align-items:center;justify-content:center;font-size:21px;font-weight:600;letter-spacing:.6px}
</style>
</head>
<body>

<!-- Outside spread -->
<section class="spread spread--outside">
  <div class="panel panel--1 steps-panel">
    <div class="steps-title__num">3</div>
    <div class="steps-title__lead">STEPS TO</div>
    <div class="steps-title__box">DENTAL<br>CARE</div>

    <div class="step" style="top:196px">
      <div class="step__pill">
        <svg class="step__icon" viewBox="0 0 30 30"><rect x="6" y="3" width="16" height="22" fill="none" stroke="#1f6fc0" stroke-width="2"/><path d="M9 9h10M9 13h10M9 17h6" stroke="#1f6fc0" stroke-width="2"/><path d="M18 24l8-10" stroke="#1f6fc0" stroke-width="3"/></svg>
        <span class="step__text">Fill out<br>Form</span>
      </div>
      <div class="step__num">1</div>
    </div>
    <div class="step" style="top:258px">
      <div class="step__pill">
        <svg class="step__icon" viewBox="0 0 30 30"><circle cx="12" cy="12" r="8" fill="none" stroke="#1f6fc0" stroke-width="2.5"/><path d="M18 18l8 8" stroke="#1f6fc0" stroke-width="3.5" stroke-linecap="round"/></svg>
        <span class="step__text">Find A<br>Dentist</span>
      </div>
      <div class="step__num">2</div>
    </div>
    <div class="step" style="top:320px">
      <div class="step__pill">
        <svg class="step__icon" viewBox="0 0 30 30"><rect x="4" y="6" width="22" height="20" rx="2" fill="none" stroke="#1f6fc0" stroke-width="2"/><path d="M4 12h22M10 3v6M20 3v6" stroke="#1f6fc0" stroke-width="2"/><path d="M10 19l3 3 6-6" fill="none" stroke="#3cb54a" stroke-width="2"/></svg>
        <span class="step__text">Get<br>Appointment</span>
      </div>
      <div class="step__num">3</div>
    </div>

    <svg class="guarantee guarantee--steps" viewBox="0 0 120 112" aria-label="100% money back guarantee">
      <path d="M60 4 L108 18 L104 66 Q96 96 60 108 Q24 96 16 66 L12 18 Z" fill="#1f6fc0" stroke="#fff" stroke-width="3"/>
      <rect x="2" y="34" width="116" height="22" fill="#fff"/>
      <text x="60" y="50" text-anchor="middle" font-family="Source Sans 3, sans-serif" font-weight="700" font-size="15" fill="#1f6fc0">GUARANTEE</text>
      <text x="60" y="78" text-anchor="middle" font-family="Source Sans 3, sans-serif" font-weight="900" font-size="20" fill="#fff">100%</text>
      <text x="60" y="92" text-anchor="middle" font-family="Source Sans 3, sans-serif" font-weight="700" font-size="10" fill="#fff">MONEY BACK</text>
    </svg>

    <p class="steps-panel__note">If you are not seen by a dentist in 24 hours or less, you will receive your money back</p>
  </div>

  <div class="brand brand--small"  style="left:342px"><span class="brand__dot"></span>Molar Relief Fast</div>

  <div class="photo photo--family" role="img" aria-label="Photo of a smiling mother with two young children"></div>

  <svg class="middle-band" viewBox="0 0 320 560" aria-hidden="true">
    <polygon points="0,330 320,250 320,262 0,342" fill="#1f6fc0"/>
    <polygon points="0,342 320,262 320,560 0,560" fill="#3cb54a"/>
  </svg>

  <svg class="service-badge" viewBox="0 0 64 80" aria-label="24 hour service">
    <rect x="2" y="2" width="60" height="76" rx="8" fill="none" stroke="#fff" stroke-width="3"/>
    <path d="M50 26 A18 18 0 1 0 50 48" fill="none" stroke="#fff" stroke-width="3"/>
    <path d="M46 20l6 6-8 2z" fill="#fff"/>
    <text x="32" y="44" text-anchor="middle" font-family="Source Sans 3, sans-serif" font-weight="700" font-size="20" fill="#fff">24</text>
    <text x="32" y="64" text-anchor="middle" font-family="Source Sans 3, sans-serif" font-weight="700" font-size="9" fill="#fff">HOUR</text>
    <text x="32" y="73" text-anchor="middle" font-family="Source Sans 3, sans-serif" font-weight="700" font-size="9" fill="#fff">SERVICE</text>
  </svg>
  <div class="middle-url">www.molarrelieffast.net</div>

  <h1 class="cover-title">
    <div class="cover-title__your">Your</div>
    <div class="cover-title__emergency">Emergency</div>
    <div class="cover-title__dentist">DENTIST</div>
  </h1>

  <div class="cover-logo">
    <div class="brand brand--large"><span class="brand__dot"></span>Molar Relief Fast</div>
    <div class="cover-url">www.molarrelieffast.net</div>
  </div>

  <span class="fold" style="left:320px"></span>
  <span class="fold" style="left:640px"></span>
</section>

<!-- Inside spread -->
<section class="spread spread--inside">
  <div class="panel panel--1 about">
    <p class="green">Our mission plain and simple is to get you seen by a qualified dentist as quickly as possible to get you out of pain.</p>
    <p class="blue">Nobody likes pain and no one should have to live with it. If we can get you seen by a dentist in 24 hours or less, we have succeeded.</p>
    <p class="lead">What we strive for is a quicker, more reliable method for patients to access their dental professional.</p>
    <p class="green">Going to the local hospitals' Emergency Department for a tooth ache will not solve the issue, hospitals are often times not equipped to handle dental emergencies and do not have dentists on staff. You leave with antibiotics and pain medication, not a solution to the real underlying problem. Leave here confident, knowing you will see a dentist in less than 24 hours!</p>
    <div class="brand brand--about"><span class="brand__dot"></span>Molar Relief Fast</div>
  </div>

  <div class="inside-green"></div>
  <p class="inside-heading">If you are not seen by a dentist in 24 hours or less, you will receive your money back</p>

  <div class="photo photo--presenter" role="img" aria-label="Photo of a woman in a business suit presenting the list"></div>

  <div class="issue issue--1"><div class="issue__box">Broken or<br>Fractured<br>Filling</div><div class="issue__num">1</div></div>
  <div class="issue issue--3"><div class="issue__box">Discolored or<br>Odd Looking<br>Tooth</div><div class="issue__num">3</div></div>
  <div class="issue issue--5"><div class="issue__box">Loose<br>Tooth</div><div class="issue__num">5</div></div>
  <div class="issue issue--2"><div class="issue__box">Broken or<br>Fractured<br>Tooth</div><div class="issue__num">2</div></div>
  <div class="issue issue--4"><div class="issue__box">Just Pain in<br>My Tooth</div><div class="issue__num">4</div></div>
  <div class="issue issue--6"><div class="issue__box">Swelling</div><div class="issue__num">6</div></div>

  <svg class="guarantee guarantee--inside" viewBox="0 0 120 112" style="left:846px" aria-label="100% money back guarantee">
    <path d="M60 4 L108 18 L104 66 Q96 96 60 108 Q24 96 16 66 L12 18 Z" fill="#1f6fc0" stroke="#fff" stroke-width="3"/>
    <rect x="2" y="34" width="116" height="22" fill="#fff"/>
    <text x="60" y="50" text-anchor="middle" font-family="Source Sans 3, sans-serif" font-weight="700" font-size="15" fill="#1f6fc0">GUARANTEE</text>
    <text x="60" y="78" text-anchor="middle" font-family="Source Sans 3, sans-serif" font-weight="900" font-size="20" fill="#fff">100%</text>
    <text x="60" y="92" text-anchor="middle" font-family="Source Sans 3, sans-serif" font-weight="700" font-size="10" fill="#fff">MONEY BACK</text>
  </svg>

  <div class="service-band">24 HOUR DENTAL SERVICE - www.molarrelieffast.net</div>

  <span class="fold" style="left:320px"></span>
  <span class="fold" style="left:640px"></span>
</section>

</body>
</html>
```